Business Card Kelda Law llc examples and ideas are attached.

in addition to the logo we need a desription what we do: "Reprsenting students with disabilites obtain services to progress in the public school system."

If you can squeeze it on the fron at the bottom great if not put it on the back

```html
<!DOCTYPE html>
<html lang="en">
<head>
<meta charset="utf-8">
<title>Kelda Law LLC — Business Card</title>
<link rel="stylesheet" href="https://fonts.googleapis.com/css2?family=Tinos:wght@400;700&family=Roboto:wght@400;500&display=swap">
<style>
  :root{
    --navy:#164f86;
    --navy-deep:#0d3a68;
    --navy-dark:#0a2f57;
    --emboss:#1c5a95;
    --paper:#f7f7f7;
    --ink:#2a2a2a;
    --grey:#6b6b6b;
    --rule:#9a9a9a;
    --soft:#c9d8e8;
    --stage:#1b1b1b;
  }
  *{margin:0;padding:0;box-sizing:border-box}
  html,body{width:1200px;height:1200px;overflow:hidden;background:var(--stage)}
  .canvas{position:relative;width:1200px;height:1200px}
  .card{position:absolute;left:160px;width:880px;height:503px;overflow:hidden;box-shadow:0 18px 40px rgba(0,0,0,.55)}
  .card--front{top:70px;background:var(--paper)}
  .card--back{top:627px;background:linear-gradient(160deg,var(--navy) 0%,var(--navy-deep) 60%,var(--navy-dark) 100%)}

  .brand{position:absolute;left:40px;top:150px;width:410px;text-align:center}
  .brand__mark{display:block;margin:0 auto 20px;width:70px;height:70px;border:3px solid var(--navy)}
  .brand__name{font-family:"Tinos",serif;font-weight:700;font-size:42px;letter-spacing:1px;color:var(--navy);white-space:nowrap}

  .divider{position:absolute;left:485px;top:110px;width:1px;height:270px;background:var(--rule)}

  .contact{position:absolute;left:525px;top:118px;width:330px}
  .contact__name{font-family:"Tinos",serif;font-weight:700;font-size:37px;color:var(--navy);line-height:1.1}
  .contact__title{font-family:"Tinos",serif;font-size:21px;color:var(--grey);margin:4px 0 26px}
  .contact__address{font-family:"Roboto",sans-serif;font-size:19px;color:var(--ink);line-height:1.4;margin-bottom:20px}
  .contact__address sup{font-size:11px}
  .contact__line{display:flex;align-items:center;gap:10px;font-family:"Roboto",sans-serif;font-size:19px;color:var(--ink);line-height:1.5;white-space:nowrap}
  .contact__line svg{width:18px;height:18px;fill:var(--ink);flex:none}

  .band{position:absolute;left:0;bottom:0;width:100%;height:56px;background:var(--navy);display:flex;align-items:center;padding-left:160px}
  .band__text{font-family:"Roboto",sans-serif;font-size:20px;color:#fff;letter-spacing:.3px}

  .back-brand{position:absolute;inset:0;display:flex;flex-direction:column;align-items:center;justify-content:center;padding-bottom:40px}
  .back-brand__mark{width:100px;height:100px;border:3px solid var(--emboss);margin-bottom:26px}
  .back-brand__name{font-family:"Tinos",serif;font-weight:700;font-size:64px;letter-spacing:2px;color:var(--emboss);white-space:nowrap}
  .back-brand__about{position:absolute;left:100px;right:100px;bottom:48px;text-align:center;font-family:"Roboto",sans-serif;font-size:20px;line-height:1.45;color:var(--soft)}
</style>
</head>
<body>
<main class="canvas">
  <section class="card card--front" aria-label="Business card front">
    <div class="brand">
      <span class="brand__mark" aria-hidden="true"></span>
      <div class="brand__name">KELDA LAW LLC</div>
    </div>
    <div class="divider"></div>
    <div class="contact">
      <h1 class="contact__name">Tomas R Kelda</h1>
      <p class="contact__title">Attorney at Law</p>
      <p class="contact__address">1450 NW 18<sup>th</sup> Ave<br>Harbor Point FL 33410</p>
      <p class="contact__line">
        <svg viewBox="0 0 24 24" aria-hidden="true"><path d="M6.6 10.8a15.1 15.1 0 0 0 6.6 6.6l2.2-2.2c.3-.3.7-.4 1-.2 1.1.4 2.3.6 3.6.6.6 0 1 .4 1 1V20c0 .6-.4 1-1 1A17 17 0 0 1 3 4c0-.6.4-1 1-1h3.5c.6 0 1 .4 1 1 0 1.3.2 2.5.6 3.6.1.3 0 .7-.2 1z"/></svg>
        555 014 2278
      </p>
      <p class="contact__line">
        <svg viewBox="0 0 24 24" aria-hidden="true"><path d="M3 5h18v14H3zm2 2v.5l7 4.5 7-4.5V7zm0 2.9V17h14V9.9l-7 4.5z"/></svg>
        tom.keldalaw@example.com
      </p>
    </div>
    <div class="band"><span class="band__text">Special Education and Related Services Law</span></div>
  </section>

  <section class="card card--back" aria-label="Business card back">
    <div class="back-brand">
      <span class="back-brand__mark" aria-hidden="true"></span>
      <div class="back-brand__name">KELDA LAW LLC</div>
    </div>
    <p class="back-brand__about">Representing students with disabilities to obtain services to progress in the public school system.</p>
  </section>
</main>
</body>
</html>
```